QuoteMarlin.com Homepage Redesign

Create a new homepage design for our website QuoteMarlin.com. Our current experience is focused on auto insurance only. We would like to incorporate the ability to receive rate estimates for home insurance and bundled (home + auto) insurance in addition to auto. Home insurance will include home, renters and condo. The final design should inspire users to utilize our comparison tool.

Industry/Entity Type

Insurance (Auto & Home)

Number of Pages Required

1 page

Font styles to use
Other font styles liked:
• See Assets - Sans Serif & Roboto

Colors
0054AA
0677BA
7BADD7
CADEEF
E8F1F8
59FF00
82FF00
B8FF75
E3FFCB
F4FFEA

Requirements
Must have
• Must include the ability to launch our rate comparison tool within the main hero image for Auto, Home, Bundled.
Nice to have
• The design should be bold and eye catching. It should be differentiated from the typical landing page experience. (Some of our favorite sites from a UX perspective include: Vaultline.org, ThePelican.com, Ferrow.com and Corvane Airways - They are busy but we like the app like approach on the homepage)
Should not have
• We are not looking for a design that is heavy on generic images.

```html
<!DOCTYPE html>
<html lang="en">
<head>
<meta charset="utf-8">
<title>Quote Marlin — Compare Home, Car &amp; Life Insurance Rates</title>
<link href="https://fonts.googleapis.com/css2?family=Sora:wght@400;600;700&family=Poppins:wght@300;400;500;600&display=swap" rel="stylesheet">
<style>
:root{
  --navy:#0c1f4e;
  --navy-2:#0a2a78;
  --blue:#0f55e0;
  --blue-bright:#1665ff;
  --blue-soft:#7badd7;
  --ice:#e8f1f8;
  --green:#6fd43f;
  --green-bright:#82ff00;
  --green-soft:#b8ff75;
  --ink:#16295a;
  --text:#5b6685;
  --line:#e4e9f2;
  --white:#ffffff;
}
*{box-sizing:border-box;margin:0;padding:0}
html,body{width:1200px;height:4274px;overflow:hidden}
body{font-family:"Poppins",sans-serif;color:var(--ink);background:var(--white);position:relative}
h1,h2,h3,.display{font-family:"Sora",sans-serif}
.abs{position:absolute}
.btn{display:inline-flex;align-items:center;gap:8px;background:var(--blue-bright);color:var(--white);font-family:"Sora",sans-serif;font-weight:600;font-size:11px;letter-spacing:.4px;border-radius:20px;padding:0 22px;height:34px;text-transform:uppercase}
.btn .arrow{width:14px;height:14px;border:1.5px solid #fff;border-radius:50%;display:inline-flex;align-items:center;justify-content:center;font-size:9px}
.hl-green{color:var(--green)}
.hl-blue{color:var(--blue-bright)}

/* header & hero */
.hero-bg{left:0;top:0;width:1200px;height:580px}
.nav{left:65px;top:18px;width:1055px;height:34px;display:flex;align-items:center;justify-content:space-between;color:#fff}
.brand{display:flex;align-items:center;gap:8px;font-family:"Sora",sans-serif;font-weight:600;font-size:19px;color:#fff}
.brand .dot{width:14px;height:14px;border-radius:50%;background:var(--blue-bright)}
.nav ul{display:flex;gap:36px;list-style:none;font-size:12.5px;font-weight:500;margin-left:auto;margin-right:36px}
.nav .btn{height:28px;padding:0 18px;font-size:10px}
.hero-copy{left:65px;top:180px;color:#fff}
.hero-copy .kicker{font-size:12px;font-weight:600}
.hero-copy h1{font-size:42px;line-height:50px;font-weight:600;margin-top:12px;width:520px}
.hero-copy p{font-size:13px;opacity:.85;margin-top:12px}
.hero-copy .btn{margin-top:18px}
.hero-art{left:407px;top:355px;width:655px;height:218px;border-radius:120px 120px 0 0;background:linear-gradient(90deg,#4fb95a,#f2b84b 35%,#9dc6ee 70%,#46b06a)}
.quote-panel{left:607px;top:120px;width:488px;height:361px;background:#1b49b4;border:1px solid rgba(255,255,255,.2);border-radius:4px;color:#fff;padding:14px 18px}
.quote-panel h3{font-size:12px;text-align:center;font-weight:600;letter-spacing:.3px}
.tabs{position:relative;display:flex;justify-content:space-around;margin-top:22px;padding:0 40px}
.tabs:before{content:"";position:absolute;left:-18px;right:-18px;top:20px;height:1px;background:rgba(255,255,255,.5)}
.tab{position:relative;text-align:center;font-size:9.5px}
.tab i{display:block;width:42px;height:42px;border-radius:50%;margin:0 auto 6px;background:#5e7fc9;border:2px solid #fff}
.tab.active i{background:var(--blue-soft);border-color:var(--green-bright)}
.form-grid{display:grid;grid-template-columns:1fr 1fr;column-gap:8px;row-gap:14px;margin-top:22px}
.field .box{height:32px;background:rgba(255,255,255,.14);border-radius:2px;font-size:9px;color:rgba(255,255,255,.6);padding:0 9px;display:flex;align-items:center}
.field label{display:block;font-size:9px;margin-top:6px}
.yesno{display:grid;grid-template-columns:1fr 1fr;gap:6px}
.yesno .box{justify-content:center;color:#fff}
.see{height:32px;background:rgba(255,255,255,.2);display:flex;align-items:center;justify-content:center;font-size:9.5px;font-weight:500}

/* decisions */
.decisions h2{left:79px;top:672px;font-size:35px;line-height:49px;font-weight:600;width:480px}
.feature{left:80px;width:500px}
.feature .ico{position:absolute;left:0;top:0;width:36px;height:36px;border-radius:50%;background:linear-gradient(135deg,#ffcb3d,#ef4444 55%,#2b63d9)}
.feature h4{margin-left:59px;font-size:13.5px;font-weight:500;color:var(--navy)}
.feature p{margin-left:59px;font-size:13px;line-height:23px;color:var(--text);margin-top:9px}
.phone-art{left:640px;top:690px;width:560px;height:630px;border-radius:44px 0 0 0;background:linear-gradient(160deg,#f7d7c0,#e9b395 60%,#fdf2ea)}
.fade{left:0;top:1320px;width:1200px;height:80px;background:linear-gradient(#fff,#f3f7fc,#fff)}

/* steps */
.steps-head{left:0;top:1380px;width:1200px;text-align:center}
.steps-head h2{font-size:35px;line-height:50px;font-weight:600}
.steps-head .tag{display:inline-block;background:var(--green-soft);font-size:10.5px;padding:1px 4px;margin-top:8px;color:var(--navy)}
.step{top:1545px;width:240px;text-align:center}
.step .ico{width:52px;height:52px;border-radius:50%;margin:0 auto;background:linear-gradient(135deg,#b8ff75,#6fd43f 60%,#f5c43b)}
.step h4{font-family:"Sora",sans-serif;font-size:11.5px;font-weight:600;margin-top:27px;color:var(--navy)}
.step p{font-size:11.5px;line-height:20px;color:var(--text);margin-top:8px}

/* curtain */
.curtain-bg{left:0;top:1866px;width:1200px;height:570px}
.dash{left:61px;top:1838px;width:537px;height:615px;background:#f5f8fd;border-radius:8px;box-shadow:0 20px 50px rgba(10,30,80,.25);padding:20px;font-size:8px;color:var(--text)}
.dash .mini-brand{font-family:"Sora",sans-serif;font-size:8px;font-weight:600;color:var(--navy);display:flex;align-items:center;gap:4px}
.dash .mini-brand i{width:7px;height:7px;border-radius:50%;background:var(--blue-bright)}
.dash .back{position:absolute;left:22px;top:56px;border:1px solid #8a95b0;border-radius:10px;padding:2px 14px;font-size:6.5px;color:var(--navy)}
.dash .side{position:absolute;left:22px;top:100px;width:170px;height:110px;background:#fff;border-radius:4px;padding:10px;font-size:5.5px;line-height:13px}
.dash .side b{display:block;margin-top:8px;background:var(--blue-bright);color:#fff;border-radius:6px;text-align:center;font-weight:500}
.dash .range{position:absolute;left:180px;top:55px;width:330px;text-align:center}
.dash .range h5{font-size:8.5px;color:var(--navy);font-weight:600}
.dash .range small{display:block;font-size:5px;margin-top:2px}
.track{position:relative;height:2px;background:var(--blue-bright);margin:22px 0 0}
.track i{position:absolute;top:-4px;width:9px;height:9px;border-radius:50%;border:2px solid var(--green);background:#fff}
.dash .results-title{position:absolute;left:180px;top:180px;font-size:8.5px;color:var(--navy);font-weight:600}
.dash .results-sub{position:absolute;left:180px;top:193px;font-size:5px}
.result{position:absolute;left:180px;width:265px;height:100px;background:#fff;border-radius:4px;padding:9px 12px}
.result .carrier{position:absolute;left:-18px;top:16px;width:22px;height:22px;border-radius:50%;background:#fff;box-shadow:0 2px 6px rgba(0,0,0,.12)}
.result h6{font-size:8px;color:var(--navy);font-weight:600}
.result .pill{display:inline-block;margin-top:3px;background:var(--green);color:#fff;font-size:4.5px;padding:1px 6px;border-radius:5px}
.result .b1,.result .b2{position:absolute;right:12px;width:64px;height:11px;border-radius:4px;font-size:5px;display:flex;align-items:center;justify-content:center}
.result .b1{top:9px;background:var(--blue-bright);color:#fff}
.result .b2{top:24px;border:1px solid var(--blue-bright);color:var(--navy)}
.result .track{margin:28px 0 0;width:235px;background:linear-gradient(90deg,var(--green),#f5c43b,#ef4444)}
.result .track i{left:30px}
.curtain-copy{left:674px;top:1930px;width:440px;color:#fff}
.curtain-copy h2{font-size:35px;line-height:52px;font-weight:600}
.curtain-copy p{font-size:12px;line-height:20px;opacity:.85;margin-top:18px}
.curtain-copy .btn{margin-top:28px}

/* compare */
.compare-head{left:0;top:2535px;width:1200px;text-align:center}
.compare-head h2{font-size:35px;line-height:44px;font-weight:600;color:var(--navy)}
.compare-head p{font-size:11.5px;line-height:19px;color:var(--text);width:880px;margin:34px auto 0}
.table-card{left:198px;top:2742px;width:803px;height:417px;background:#fff;box-shadow:0 10px 40px rgba(20,50,120,.1);padding:28px 74px}
.table-card table{width:100%;border-collapse:collapse;font-size:11.5px;color:var(--navy)}
.table-card th{height:50px;font-size:12px;font-weight:600;vertical-align:middle}
.table-card th.us{color:var(--navy);font-family:"Sora",sans-serif}
.table-card th.them{color:var(--navy);font-family:"Sora",sans-serif}
.table-card td{height:46px;border-bottom:1px solid var(--line)}
.table-card tr:last-child td{border-bottom:none}
.table-card td.c{text-align:center;width:155px;color:#9aa4bb}
.tick{display:inline-block;width:12px;height:12px;border-radius:50%;border:1.5px solid var(--green);vertical-align:middle;position:relative}
.tick.blue{border-color:var(--blue-bright)}
.tick:after{content:"";position:absolute;left:3px;top:1px;width:3px;height:5px;border:solid var(--green);border-width:0 1.5px 1.5px 0;transform:rotate(45deg)}
.tick.blue:after{border-color:var(--blue-bright)}

/* faq */
.faq h2{left:0;top:3236px;width:1200px;text-align:center;font-size:35px;font-weight:600;color:var(--navy)}
.faq-item{left:257px;width:686px;height:58px;border:1px solid var(--line);border-radius:3px;display:flex;align-items:center;justify-content:space-between;padding:0 45px 0 20px;font-size:11px;color:var(--navy)}
.faq-item span{color:var(--blue-bright);font-size:14px}

/* cta */
.cta{left:257px;top:3826px;width:686px;height:178px;background:#f3f6fb;border:1px solid var(--line);border-radius:3px}
.cta h2{position:absolute;left:61px;top:44px;font-size:27px;font-weight:600;color:var(--navy)}
.cta p{position:absolute;left:61px;top:88px;font-size:10.5px;color:var(--navy)}
.cta .zip{position:absolute;left:61px;top:114px;display:flex;height:32px;box-shadow:0 4px 12px rgba(0,0,0,.06)}
.cta .zip span{width:155px;background:#fff;font-size:9px;color:#9aa4bb;display:flex;align-items:center;padding-left:10px}
.cta .zip b{width:100px;background:var(--blue-bright);color:#fff;font-size:9.5px;font-family:"Sora",sans-serif;font-weight:600;display:flex;align-items:center;justify-content:center}
.dog-art{position:absolute;right:40px;top:-36px;width:168px;height:212px;border-radius:80px 80px 0 0;background:linear-gradient(160deg,#f0c27a,#d4903e 60%,#f6d34a)}

/* footer */
.footer-bg{left:0;top:4030px;width:1200px;height:244px}
.footer-brand{left:190px;top:4104px;width:240px;color:#fff}
.footer-brand .brand{font-size:21px}
.footer-brand p{font-size:10px;line-height:15px;margin-top:24px;opacity:.85}
.fcol{top:4096px;color:#fff}
.fcol h5{font-family:"Sora",sans-serif;font-size:14px;font-weight:600}
.fcol ul{list-style:none;font-size:10px;line-height:22px;margin-top:16px;opacity:.9}
.badge{left:805px;top:4095px;width:40px;height:40px;border-radius:50%;background:#e8edf6;border:3px solid #c9d3e6}
.states{left:805px;top:4150px;color:#fff}
.states h6{font-size:10px;font-weight:600}
.states div{display:grid;grid-template-columns:repeat(10,28px);font-size:9.5px;line-height:20px;margin-top:8px}
.copyright{left:0;top:4247px;width:1200px;text-align:center;font-size:9px;color:rgba(255,255,255,.7)}
</style>
</head>
<body>

<!-- HERO -->
<svg class="abs hero-bg" viewBox="0 0 1200 580" aria-hidden="true">
  <defs>
    <linearGradient id="heroGrad" x1="0" y1="0" x2="1" y2="1">
      <stop offset="0" stop-color="#0c1f4e"/>
      <stop offset="0.6" stop-color="#0c3a9e"/>
      <stop offset="1" stop-color="#1060ff"/>
    </linearGradient>
  </defs>
  <path d="M0 0H1200V520C900 540 500 540 0 566Z" fill="url(#heroGrad)"/>
</svg>

<header class="abs nav">
  <div class="brand"><span class="dot"></span>Quote Marlin</div>
  <ul><li>Car Insurance</li><li>Home Insurance</li><li>Life Insurance</li><li>Resources</li><li>Company</li></ul>
  <span class="btn">Compare <span class="arrow">›</span></span>
</header>

<div class="abs hero-copy">
  <div class="kicker">Quick. Private. Reliable Results.</div>
  <h1>Compare Home, Car &amp; life&nbsp; Insurance Rates</h1>
  <p>See what you should pay at top companies near you</p>
  <span class="btn">Compare Rates <span class="arrow">›</span></span>
</div>

<div class="abs hero-art" role="img" aria-label="Illustration of a yellow car parked by green trees and a house"></div>

<div class="abs quote-panel">
  <h3>COMPARE SPAM FREE ALWAYS</h3>
  <div class="tabs">
    <div class="tab active"><i></i>Combined</div>
    <div class="tab"><i></i>Auto</div>
    <div class="tab"><i></i>Home</div>
  </div>
  <div class="form-grid">
    <div class="field"><div class="box">Enter ZIP Code</div><label>ZIP Code</label></div>
    <div class="field"><div class="box">Enter Your Age</div><label>How Old Are You?</label></div>
    <div class="field"><div class="box">Enter your current provider</div><label>Current Provider</label></div>
    <div class="field"><div class="box">Chose your credit score</div><label>Credit Score</label></div>
    <div class="field"><div class="yesno"><div class="box">YES</div><div class="box">NO</div></div><label>Do You Own A Home?</label></div>
    <div class="field"><div class="see">SEE RESULTS</div></div>
  </div>
</div>

<!-- DECISIONS -->
<section class="decisions">
  <h2 class="abs">Everything you need to make the <span class="hl-green">right decisions</span></h2>
  <div class="abs feature" style="top:805px">
    <span class="ico"></span>
    <h4>No bait and switch – accurate rate estimates using better data</h4>
    <p>No low-ball quotes. We use the rating plans submitted by each insurance carrier to the state department of insurance plus any applicable discounts to more accurately calculate what you can expect to pay.</p>
  </div>
  <div class="abs feature" style="top:968px">
    <span class="ico"></span>
    <h4>More choices – not limited to paid advertisers</h4>
    <p>Unlike other sites, our results are not limited to paid sponsors. Our results represent top carriers in your geographic area based on the total premiums written.</p>
  </div>
  <div class="abs feature" style="top:1107px">
    <span class="ico"></span>
    <h4>Spam-free - no contact information required</h4>
    <p>We are the only insurance comparison tool that does not require your contact information to generate your estimates, so you can be sure you won't get spam from us.</p>
  </div>
  <div class="abs phone-art" role="img" aria-label="Photo of a hand holding a phone showing recommended insurance results"></div>
</section>
<div class="abs fade"></div>

<!-- STEPS -->
<section>
  <div class="abs steps-head">
    <h2><span class="hl-green">Insurance shopping</span> can be pleasant - like<br>a relaxing scroll through the - <span class="hl-blue">best rates</span></h2>
    <span class="tag">Start saving in 3 simple steps</span>
  </div>
  <div class="abs step" style="left:176px"><div class="ico"></div><h4>QUICK START</h4><p>Answer 5 questions No phone number or email required.</p></div>
  <div class="abs step" style="left:478px"><div class="ico"></div><h4>RETRIEVE YOUR RATES</h4><p>We estimate how much you'll pay at each top provider in your state.</p></div>
  <div class="abs step" style="left:777px"><div class="ico"></div><h4>COMPARE AND SAVE</h4><p>Compare apples to apples pricing to find your next provider.</p></div>
  <span class="abs btn" style="left:524px;top:1722px">Compare Rates <span class="arrow">›</span></span>
</section>

<!-- CURTAIN -->
<svg class="abs curtain-bg" viewBox="0 0 1200 570" aria-hidden="true">
  <defs>
    <linearGradient id="curtainGrad" x1="0" y1="0" x2="1" y2="0">
      <stop offset="0" stop-color="#0a3fb8"/>
      <stop offset="1" stop-color="#0c2a78"/>
    </linearGradient>
  </defs>
  <path d="M0 0H1200V220C1080 420 820 500 560 540H0Z" fill="url(#curtainGrad)"/>
  <path d="M560 540C820 500 1080 420 1200 220V250C1080 440 830 520 560 550Z" fill="#1060ff" opacity=".6"/>
</svg>

<div class="abs dash">
  <div class="mini-brand"><i></i>Quote Marlin</div>
  <span class="back">‹ Go Back</span>
  <div class="side">Edit your details to refine estimates<br>Home Basics<br>Vehicle details<br>Discount savings<b>Personalize profile</b></div>
  <div class="range">
    <h5>Range of Annual Rates</h5>
    <small>Rates estimated from filed state rating plans</small>
    <div class="track"><i style="left:0"></i><i style="left:48%"></i><i style="right:0"></i></div>
  </div>
  <div class="results-title">Your Results</div>
  <div class="results-sub">Carriers ranked by estimated yearly premium in your state</div>
  <div class="result" style="top:215px"><span class="carrier"></span><h6>Brightshore</h6><span class="pill">Best value</span><span class="b1">Get quote</span><span class="b2">Call now</span><div class="track"><i></i></div></div>
  <div class="result" style="top:330px"><span class="carrier"></span><h6>Meadowgate</h6><span class="pill">Top rated</span><span class="b1">Online quote</span><span class="b2">Talk to agent</span><div class="track"><i></i></div></div>
  <div class="result" style="top:445px"><span class="carrier"></span><h6>Keystead</h6><span class="pill">Low cost</span><span class="b1">Get quote</span><span class="b2">Call now</span><div class="track"><i></i></div></div>
</div>

<div class="abs curtain-copy">
  <h2>Lifting the curtain <span class="hl-green">on the insurance industry</span></h2>
  <p>Insurance companies have rating plans that detail how they use certain characteristics to assign different rates to different people. These rating plans must be approved by your state department of insurance but are not typically available to consumers.</p>
  <p>Quote Marlin uses the data from each insurance company's rating plan (plus any applicable discounts) to more accurately calculate what you can expect to pay.</p>
  <span class="btn">Start Comparing <span class="arrow">›</span></span>
</div>

<!-- COMPARE TABLE -->
<section>
  <div class="abs compare-head">
    <h2>Your free and impartial insurance<br>research tool</h2>
    <p>We're passionate about giving you open access to the data you need to make smart insurance decisions. We don't sell insurance policies directly – our tool allows you independently research your options and seamlessly connect with the provider that works for you.</p>
  </div>
  <div class="abs table-card">
    <table>
      <tr><th></th><th class="us">Quote Marlin</th><th class="them">Other Sites</th></tr>
      <tr><td>Connects you with the provider you choose</td><td class="c"><span class="tick"></span></td><td class="c"><span class="tick blue"></span></td></tr>
      <tr><td>No email or phone number required</td><td class="c"><span class="tick"></span></td><td class="c">–</td></tr>
      <tr><td>Rates for all top companies in your state</td><td class="c"><span class="tick"></span></td><td class="c">–</td></tr>
      <tr><td>Accurate rates verified with state-approved rating plans</td><td class="c"><span class="tick"></span></td><td class="c">–</td></tr>
      <tr><td>Results not limited to companies with paid sponsorships</td><td class="c"><span class="tick"></span></td><td class="c">–</td></tr>
      <tr><td>Results shown after just 5 questions</td><td class="c"><span class="tick"></span></td><td class="c">–</td></tr>
      <tr><td>Option to purchase a policy through them</td><td class="c">–</td><td class="c"><span class="tick blue"></span></td></tr>
    </table>
  </div>
</section>

<!-- FAQ -->
<section class="faq">
  <h2 class="abs">Frequently Asked</h2>
  <div class="abs faq-item" style="top:3318px">How does the insurance company determine my rate?<span>+</span></div>
  <div class="abs faq-item" style="top:3385px">How do I switch my car insurance?<span>+</span></div>
  <div class="abs faq-item" style="top:3452px">How is Quote Marlin different than other insurance websites?<span>+</span></div>
  <div class="abs faq-item" style="top:3519px">How does Quote Marlin make money?<span>+</span></div>
  <div class="abs faq-item" style="top:3586px">You say you don't limit results – why do I only see up to 12?<span>+</span></div>
  <div class="abs faq-item" style="top:3653px">How can I get cheaper car insurance?<span>+</span></div>
  <div class="abs faq-item" style="top:3720px">How much car insurance do I need?<span>+</span></div>
</section>

<!-- CTA -->
<section class="abs cta">
  <h2>Ready, set, <span class="hl-blue">retrieve</span></h2>
  <p>Ready to get started? Dig up the best insurance providers in seconds.</p>
  <div class="zip"><span>Enter ZIP Code</span><b>COMPARE NOW</b></div>
  <div class="dog-art" role="img" aria-label="Photo of a golden retriever wearing a yellow bandana"></div>
</section>

<!-- FOOTER -->
<svg class="abs footer-bg" viewBox="0 0 1200 244" aria-hidden="true">
  <defs>
    <linearGradient id="footGrad" x1="0" y1="0" x2="1" y2="1">
      <stop offset="0" stop-color="#0a3aa8"/>
      <stop offset="1" stop-color="#0c2466"/>
    </linearGradient>
  </defs>
  <path d="M0 40C400 -10 800 -10 1200 30V244H0Z" fill="url(#footGrad)"/>
</svg>

<div class="abs footer-brand">
  <div class="brand"><span class="dot"></span>Quote Marlin</div>
  <p>Quote Marlin Is Your Insurance Companion – Connecting You With Top Auto Insurance Providers Without Collecting Your Contact Information.</p>
</div>
<div class="abs fcol" style="left:475px"><h5>EXPLORE</h5><ul><li>Car Insurance</li><li>Home Insurance</li><li>Life Insurance</li><li>Insurance by state</li></ul></div>
<div class="abs fcol" style="left:644px"><h5>LINKS</h5><ul><li>Privacy Policy</li><li>Terms &amp; Conditions</li><li>How We Make Profit</li><li>Partner With Us</li></ul></div>
<div class="abs badge" aria-hidden="true"></div>
<div class="abs states">
  <h6>Find coverage in your state</h6>
  <div><span>AL</span><span>AK</span><span>AZ</span><span>AR</span><span>CO</span><span>CA</span><span>CT</span><span>DC</span><span>DE</span><span>FL</span><span>GA</span><span>HI</span><span>ID</span><span>IN</span><span>IA</span><span>KS</span><span>KY</span><span>LA</span><span>ME</span><span>MD</span></div>
</div>
<div class="abs copyright">© 2023 Quote Marlin. All rights reserved.</div>

</body>
</html>
```